STICKER DESIGN required for packaging. UK START UP TEA BUSINESS

We are looking for a design for a sticker that will be applied to packaging for our teas! We are a new start up Tea business based in the UK called 'BrookMints'
Selling quality loose leaf tea and teabags via our online shop and also face to face at farmers markets / food shows and eventually in our own tea emporium. We will be marketing our teas to hotels, cafes, delis etc. too
We carry every day teas eg. breakfast blends and also speciality and rare teas to offer customers the chance to try something new. Tea as a treat / ritual / indulgence / healthy lifestyle choice / modern
The design will initially be printed on vinyl stickers and then applied to the tea packaging (pouch bags in matte black and matte silver), in the future the design may be printed direct onto our packaging. The sticker design will need to be scalable as the size of the pouch bag varies dependant on the tea.
The sticker we have in mind is a leaf shape (sketch attached)
colour green to match our logo
It will include our logo (files attached)
Text to be included on the sticker is
- www.brookmints.co.uk
- Dellow, England
- The tea type eg. Green
It will need to complement both black and silver pouches that we are using to package our teas (see attached image of our pouches)
Colours - green leaf, see our corporate colours (green & orange) on our logo files attached. We also like silver and black.
Font - nothing to swirly, must be easy to read on the packaging
once a sticker design is agreed for the initial tea type (Green) we will require additional files for each tea type that we stock. Just the tea type (Green) to be updated - the rest of the design to stay the same. The tea types we stock are listed below
Green
Black
Oolong
White
Herbal
Blended
Happy to answer any questions and aim to give feedback daily! Thank you for your interest
Best regards

```html
<!DOCTYPE html>
<html lang="en">
<head>
<meta charset="utf-8">
<title>BrookMints Oolong Leaf Sticker</title>
<link rel="stylesheet" href="https://fonts.googleapis.com/css2?family=Nunito+Sans:wght@300;400&display=swap">
<style>
  :root {
    --backdrop-centre: #ffffff;
    --backdrop-edge: #cfcfcf;
    --leaf-green: #066a3a;
    --silver-text: #c8cdca;
    --fine-text: #d9dedb;
  }
  html, body {
    margin: 0;
    padding: 0;
    width: 1200px;
    height: 1000px;
    overflow: hidden;
  }
  body {
    background: radial-gradient(ellipse 60% 62% at 50% 50%, var(--backdrop-centre) 55%, var(--backdrop-edge) 100%);
    font-family: "Nunito Sans", "Helvetica Neue", Arial, sans-serif;
  }
  .sticker {
    display: block;
    width: 1200px;
    height: 1000px;
  }
  .leaf-shape { fill: var(--leaf-green); }
  .brand-name {
    fill: var(--silver-text);
    font-family: "Nunito Sans", "Helvetica Neue", Arial, sans-serif;
    font-weight: 300;
    font-size: 46px;
    letter-spacing: 1px;
  }
  .tea-type {
    fill: var(--silver-text);
    font-family: "Nunito Sans", "Helvetica Neue", Arial, sans-serif;
    font-weight: 300;
    font-size: 14px;
    letter-spacing: 6px;
  }
  .web-address, .location {
    fill: var(--fine-text);
    font-family: "Nunito Sans", "Helvetica Neue", Arial, sans-serif;
    font-weight: 400;
    letter-spacing: 2px;
  }
  .web-address { font-size: 16px; }
  .location { font-size: 18px; }
</style>
</head>
<body>
  <svg class="sticker" viewBox="0 0 1200 1000" xmlns="http://www.w3.org/2000/svg" aria-label="BrookMints Oolong leaf sticker">
    <path class="leaf-shape" d="M350,838 C335,780 325,680 340,590 C360,470 400,400 470,360 C560,305 700,295 800,275 C850,265 880,250 902,246 C918,244 925,256 920,270 C905,330 890,390 870,440 C830,540 760,610 670,645 C590,675 480,680 420,695 C375,708 352,730 355,770 C357,795 362,820 360,830 C358,840 352,842 350,838 Z"/>

    <text class="web-address" transform="translate(655 332) rotate(-11)">www.brookmints.co.uk</text>

    <text class="brand-name" x="603" y="538" text-anchor="middle">BrookMints</text>
    <text class="tea-type" x="583" y="570" text-anchor="middle">OOLONG</text>

    <text class="location" transform="translate(392 697) rotate(-11.5)">Dellow, England</text>
  </svg>
</body>
</html>
```